Visitenkarten für Mentorin für Frauen
Zielgruppe
Ich bin Mentorin für Frauen (30-50 Jahre alt), die ihre Berufung endlich finden möchten und sich nach mehr Energie und Sinn sehnen. Ich helfe ihnen mit meiner (Name fehtl noch)-Methode ihren Seelenweg zu finden und zu gehen, sodass sie vor Energie übersprudeln und mit einem Leuchten in den Augen ein Leben in Fluss und Fülle kreieren.
Sie sind nicht unglücklich, aber es fehtl ihnen was, das sie wirklich erfüllt.
Stichwörter: Numerologie, Human Design, Seelenweg, Berufung, Lebensaufgabe, erfüllt sein- endlich die Leere füllen, Freiheit, Selbstbestimmt, Selbstliebe, Potentialentfaltung, Transformation
meine core story:
Mit Freude, unglaublicher Energie und einem Strahlen in den Augen schon vor dem Wecker aufzustehen, war für mich früher undenkbar. Ich konnte mir nicht vorstellen, wie sich Leute auf den Montag freuen konnten.
Dabei hätte mich nicht als unglücklich bezeichnet, aber es fehlt einfach etwas, ich hatte eine innere Leere und eine Sehnsucht nach dem Sinn in meinem Lebe, wollte so geliebt werden wie ich bin und mich auch so zeigen können. Ich weiß wie es ist sich klein, unsicher zu fühlen und nicht zu wissen woher das kommt. Ich habe es einfach nicht für möglich gehalten, dass diese innere Leere so leicht zu füllen ist und Freude, Spaß, Selbstbewusstseein und Leichtigkeit in allen Bereichen mit sich bringt.
Weil ich selbst diesen Weg gegangen bin und weil ich weiß, dass es nichts erfüllenderes gibt als das schlummernde Potential zu erwecken, begleite ich Frauen dabei ihren Seelenweg zu finden und zu gehen.
Dadurch dass sie genau wissen, was ihre Gaben sind und was ihre Seele glücklich macht, haben sie Spaß und Freude, gerade auch in den alltäglichen Dingen. Sie führen ein selbstbestimmtes Leben, lieben sich selbst und zeigen sich so wie sie sind.Die gigantische Energie die dadurch in ihnen frei wird, lässt sie die bisherigen Grenzen überwinden. Sie tun was sie erfüllt, o..
Aufgabenstellung
weiblich, geschwungen, weich: beinhalten solls:
Helena Wortmann
Mentorin für Powerfrauen
(Lebe deine Berufung)--> da bin ich mir nicht ganz sicher ob das gut aussehn wird oder zuviel wird
falls relevant habe ich bisher folgende Schriftarten verwendet: Canva Sans und Tan mon cheri
ist aber kein muss

```html
<!DOCTYPE html>
<html lang="de">
<head>
<meta charset="utf-8">
<title>Helena Wortmann – Visitenkarte</title>
<link rel="stylesheet" href="https://fonts.googleapis.com/css2?family=Allura&family=Cormorant+Garamond:wght@400;500&family=Poppins:wght@300;400&display=swap">
<style>
  :root {
    --paper: #f4e5dd;
    --paper-deep: #eed8ce;
    --pattern: #ebcfc4;
    --magenta: #bd3b77;
    --ink: #4a4446;
    --ink-soft: #5b5557;
    --white: #fbf3ef;
    --rose-gold-light: #f0c6b4;
    --rose-gold: #d99a86;
    --rose-gold-dark: #c27f6b;
    --floral: #d99b8b;
  }
  html, body {
    margin: 0;
    padding: 0;
    width: 1200px;
    height: 686px;
    overflow: hidden;
    background: var(--paper);
  }
  .card {
    position: relative;
    width: 1200px;
    height: 686px;
    overflow: hidden;
    background: var(--paper);
  }
  .pattern {
    position: absolute;
    inset: 0;
    background:
      radial-gradient(ellipse at 28% 38%, rgba(250,240,234,0.9) 0%, rgba(250,240,234,0) 55%),
      linear-gradient(180deg, var(--paper) 0%, var(--pattern) 100%);
  }
  .floral {
    position: absolute;
    background: radial-gradient(ellipse at center, rgba(217,155,139,0.55) 0%, rgba(217,155,139,0.25) 45%, rgba(217,155,139,0) 72%);
  }
  .floral--top { left: 955px; top: -30px; width: 275px; height: 250px; }
  .floral--bottom { left: 1040px; top: 490px; width: 190px; height: 220px; }

  .name {
    position: absolute;
    left: 86px;
    top: 72px;
    margin: 0;
    font-family: "Allura", cursive;
    font-weight: 400;
    font-size: 108px;
    line-height: 1;
    color: var(--magenta);
    white-space: nowrap;
  }
  .role {
    position: absolute;
    left: 88px;
    top: 202px;
    margin: 0;
    font-family: "Cormorant Garamond", serif;
    font-weight: 500;
    font-size: 35px;
    line-height: 40px;
    letter-spacing: 0.22em;
    text-transform: uppercase;
    color: var(--ink);
  }
  .contact {
    position: absolute;
    left: 0;
    width: 564px;
    height: 85px;
    background: var(--magenta);
    border-radius: 0 43px 43px 0;
    box-shadow: 0 10px 18px rgba(120, 60, 70, 0.22);
  }
  .contact--phone { top: 311px; }
  .contact--web { top: 426px; }
  .contact__icon {
    position: absolute;
    left: 86px;
    top: 12px;
    width: 62px;
    height: 62px;
  }
  .contact__text {
    position: absolute;
    left: 172px;
    top: 0;
    line-height: 85px;
    font-family: "Poppins", sans-serif;
    font-weight: 300;
    font-size: 33px;
    color: var(--white);
    white-space: nowrap;
  }
  .contact--phone .contact__text { letter-spacing: 0.06em; }
  .address {
    position: absolute;
    left: 89px;
    top: 566px;
    margin: 0;
    font-family: "Cormorant Garamond", serif;
    font-weight: 500;
    font-size: 40px;
    color: var(--ink-soft);
    white-space: nowrap;
  }
  .portrait {
    position: absolute;
    left: 697px;
    top: 146px;
    width: 434px;
    height: 434px;
  }
</style>
</head>
<body>
<div class="card">
  <div class="pattern" role="img" aria-label="Dezentes Wabenmuster im Hintergrund"></div>
  <div class="floral floral--top" role="img" aria-label="Zarte florale Zweige in Roségold"></div>
  <div class="floral floral--bottom" role="img" aria-label="Zarte florale Zweige in Roségold"></div>

  <h1 class="name">Helena Wortmann</h1>
  <p class="role">Mentorin für<br>Powerfrauen</p>

  <div class="contact contact--phone">
    <svg class="contact__icon" viewBox="0 0 62 62" aria-hidden="true">
      <circle cx="31" cy="31" r="29" fill="var(--white)" stroke="var(--rose-gold)" stroke-width="2"/>
      <circle cx="31" cy="31" r="24" fill="none" stroke="var(--rose-gold-light)" stroke-width="1.5"/>
      <path d="M23 20c1.5-1.2 3.2-.8 4 .6l2 3.6c.7 1.3.3 2.6-.8 3.4l-1.3 1c1 2.6 3 4.6 5.5 5.6l1-1.3c.8-1.1 2.2-1.5 3.4-.8l3.6 2c1.4.8 1.8 2.5.6 4l-1.6 1.8c-1.4 1.4-3.6 1.8-5.6 1C27.6 38.6 23.4 34.4 21 28.2c-.8-2-.4-4.2 1-5.6z" fill="none" stroke="var(--magenta)" stroke-width="2.2" stroke-linejoin="round"/>
    </svg>
    <span class="contact__text">+49 170 482 1937</span>
  </div>

  <div class="contact contact--web">
    <svg class="contact__icon" viewBox="0 0 62 62" aria-hidden="true">
      <circle cx="31" cy="31" r="29" fill="var(--white)" stroke="var(--rose-gold)" stroke-width="2"/>
      <circle cx="31" cy="31" r="24" fill="none" stroke="var(--rose-gold-light)" stroke-width="1.5"/>
      <path d="M31 41s-10-6.2-10-12.6c0-3.2 2.4-5.4 5.2-5.4 2 0 3.8 1.2 4.8 2.9 1-1.7 2.8-2.9 4.8-2.9 2.8 0 5.2 2.2 5.2 5.4C41 34.8 31 41 31 41z" fill="var(--magenta)"/>
    </svg>
    <span class="contact__text">helenawortm.de</span>
  </div>

  <p class="address">Lindenweg 12, Rosental</p>

  <svg class="portrait" viewBox="0 0 434 434">
    <defs>
      <linearGradient id="ring-gradient" x1="0" y1="0" x2="1" y2="1">
        <stop offset="0" stop-color="var(--rose-gold-light)"/>
        <stop offset="0.5" stop-color="var(--rose-gold)"/>
        <stop offset="1" stop-color="var(--rose-gold-dark)"/>
      </linearGradient>
      <radialGradient id="photo-gradient" cx="0.5" cy="0.45" r="0.6">
        <stop offset="0" stop-color="#c98a6e"/>
        <stop offset="0.55" stop-color="#8a5340"/>
        <stop offset="1" stop-color="#3a2320"/>
      </radialGradient>
    </defs>
    <circle cx="217" cy="217" r="212" fill="url(#ring-gradient)"/>
    <circle cx="217" cy="217" r="202" fill="url(#photo-gradient)" role="img" aria-label="Porträtfoto der Mentorin mit lockigem Haar und rosé Make-up"/>
  </svg>
</div>
</body>
</html>
```